Business Card Design for Funky New Cloud Security Start-up

We're looking for kick ass business cards to make use stand out from the crowd in a world that's dominated by dull, boring, blue logos.

We have a logo (designed here on pixel forum) and we'd like to build on the brand theme of "protection kept easy."

Please use following details for sample:

Martin Colby
CEO
+61 (0)4077 518 206
mart@quenvo.com

2714/58 Harwood Street
Sydney NSW 2000
Australia

Target Market(s)

Customers will be large enterprise clients - typically VP level. Also resellers of our product who are mid-tier.

Industry/Entity Type

Business

Font styles to use
Sans Serif

Requirements
Must have
• Use the colour scheme from the attached logo
Do not put space for a fax - it's old school
Easy to use on nova press
Use a font that complements the logo font

```html
<!DOCTYPE html>
<html lang="en">
<head>
<meta charset="utf-8">
<title>quenvo – business cards</title>
<link rel="stylesheet" href="https://fonts.googleapis.com/css2?family=Arimo:wght@400;700&display=swap">
<style>
  :root {
    --stage: #a4a5a8;
    --stage-light: #c4c5c8;
    --card-dark: #1b1b1c;
    --card-dark-soft: #2a2a2b;
    --card-light: #ffffff;
    --brand-blue: #1e9ad6;
    --brand-green: #8cc63f;
    --ink: #4a4a4a;
    --ink-soft: #6b6b6b;
    --rule: #9a9a9a;
    --white: #ffffff;
  }
  * { box-sizing: border-box; margin: 0; padding: 0; }
  html, body {
    width: 1200px; height: 900px; overflow: hidden;
  }
  body {
    background: radial-gradient(ellipse at 50% 35%, var(--stage-light), var(--stage) 75%);
    font-family: "Arimo", Arial, sans-serif;
    position: relative;
  }
  .card {
    position: absolute;
    left: 300px;
    width: 600px;
    height: 343px;
    border-radius: 2px;
    box-shadow: 0 8px 22px rgba(0,0,0,.25);
    overflow: hidden;
  }

  /* Front */
  .card-front { top: 70px; background: var(--card-dark); }
  .card-front .pattern-fill {
    position: absolute; inset: 0;
    background: linear-gradient(135deg, var(--card-dark-soft), var(--card-dark) 70%);
  }
  .card-front .brand {
    position: absolute; left: 60px; top: 150px;
    display: flex; align-items: flex-end; gap: 12px;
  }
  .card-front .brand-name {
    color: var(--white); font-size: 96px; font-weight: 400;
    line-height: .8; letter-spacing: -1px;
  }
  .card-front .brand-dot {
    width: 20px; height: 20px; border-radius: 50%;
    background: var(--brand-green); margin-bottom: 2px;
  }
  .card-front .tagline {
    position: absolute; left: 62px; top: 246px;
    color: var(--white); font-size: 29px; font-weight: 700;
    letter-spacing: .3px; white-space: nowrap;
  }

  /* Back */
  .card-back { top: 487px; background: var(--card-light); }
  .card-back .brand {
    position: absolute; left: 50px; top: 146px;
    display: flex; align-items: center; gap: 12px;
  }
  .card-back .brand-dot {
    width: 34px; height: 34px; border-radius: 50%;
    background: var(--brand-blue);
  }
  .card-back .brand-name {
    color: var(--ink); font-size: 48px; font-weight: 400; letter-spacing: -.5px;
  }
  .card-back .divider {
    position: absolute; left: 318px; top: 48px;
    width: 1px; height: 160px; background: var(--rule);
  }
  .contact {
    position: absolute; left: 338px; top: 42px;
    color: var(--ink-soft); font-size: 13px; line-height: 1.35;
    white-space: nowrap;
  }
  .contact .person-name {
    color: var(--brand-blue); font-size: 21px; font-weight: 700; letter-spacing: .5px;
  }
  .contact .person-role { margin-bottom: 14px; }
  .contact .label { color: var(--brand-blue); }
  .contact .address { margin-top: 16px; }
</style>
</head>
<body>

  <section class="card card-front" aria-label="Card front">
    <div class="pattern-fill" role="img" aria-label="Dark repeating wordmark texture"></div>
    <div class="brand">
      <span class="brand-name">quenvo</span>
      <span class="brand-dot"></span>
    </div>
    <p class="tagline">protection kept easy</p>
  </section>

  <section class="card card-back" aria-label="Card back">
    <div class="brand">
      <span class="brand-dot"></span>
      <span class="brand-name">quenvo</span>
    </div>
    <div class="divider"></div>
    <div class="contact">
      <p class="person-name">Martin Colby</p>
      <p class="person-role">CEO</p>
      <p><span class="label">P:</span> +61 (0)4077 518 206</p>
      <p><span class="label">E:</span> mart@quenvo.com</p>
      <p>www.quenvo.com</p>
      <p class="address">2714/58 Harwood Street<br>Sydney NSW 2000<br>Australia</p>
    </div>
  </section>

</body>
</html>
```